Velvet Crypt Mixtape Podcast Design

My audio drama podcast is a funny horror story with romantic elements called Velvet Crypt Mixtape.
I'm looking for a colorful design featuring the title and letting the viewer know this is a horror show.
The title needs to be clearly visible even in thumbnail size.

```html
<!DOCTYPE html>
<html lang="en">
<head>
<meta charset="utf-8">
<title>Velvet Crypt Mixtape — Podcast Cover</title>
<link rel="stylesheet" href="https://fonts.googleapis.com/css2?family=Bebas+Neue&family=Permanent+Marker&display=swap">
<style>
  :root {
    --stage: #e4e4e4;
    --ink: #111111;
    --pumpkin: #d35d0a;
    --moon: #ffffff;
  }
  html, body {
    margin: 0;
    padding: 0;
    width: 1200px;
    height: 807px;
    overflow: hidden;
    background: var(--stage);
  }
  .canvas {
    position: relative;
    width: 1200px;
    height: 807px;
  }
  .cover {
    position: absolute;
    left: 240px;
    top: 43px;
    width: 720px;
    height: 720px;
    background: var(--ink);
    overflow: hidden;
  }
  .cover-scene {
    position: absolute;
    inset: 0;
    width: 720px;
    height: 720px;
  }
  .cover-title {
    position: absolute;
    left: 0;
    right: 0;
    top: 78px;
    margin: 0;
    display: flex;
    flex-direction: column;
    align-items: center;
    color: var(--ink);
    font-weight: 400;
  }
  .title-line {
    display: block;
    font-family: "Bebas Neue", "Oswald", sans-serif;
    line-height: 0.86;
    letter-spacing: 2px;
    text-shadow: 5px 7px 0 var(--pumpkin);
  }
  .title-line--top { font-size: 170px; }
  .title-line--main { font-size: 200px; }
  .title-line--script {
    font-family: "Permanent Marker", cursive;
    font-size: 104px;
    line-height: 1.1;
    letter-spacing: 4px;
    margin-top: 10px;
    text-shadow: none;
  }
</style>
</head>
<body>
  <main class="canvas">
    <section class="cover">
      <svg class="cover-scene" viewBox="0 0 720 720" role="img"
           aria-label="Halloween night scene: weathered orange wooden fence, full white moon, flying bats and gravestone silhouettes on a dark hill">
        <rect x="0" y="0" width="720" height="720" fill="var(--ink)"/>
        <rect x="12" y="12" width="696" height="600" fill="var(--pumpkin)"/>
        <circle cx="360" cy="443" r="278" fill="var(--moon)"/>
        <rect x="0" y="600" width="720" height="120" fill="var(--ink)"/>
      </svg>
      <h1 class="cover-title">
        <span class="title-line title-line--top">Velvet</span>
        <span class="title-line title-line--main">Crypt</span>
        <span class="title-line title-line--script">MIXTAPE</span>
      </h1>
    </section>
  </main>
</body>
</html>
```